Willowmere Acres Brand - Bag Design

We are a company dealing with nuts, grains and seeds and are looking for a design for our retail bag packaging that will be consistent across all our product range. We are currently differentiating in way of color but please feel free to be more creative if you wish. Sample of products include pumpkin seeds, rolled oats, almonds, etc.
Design Idea: Hygienic, Natural (from Nature), Quality & Upscale, Simple & Clean design
Target Market: High-end Markets, end-users of A/B type.
1. Bag size is 210 mm (width) * 310 mm (length). Material is OPP or multi-layer PP.
2. Front must have clear window to show packed products. Back clear window is optional.
3. Front side must have logo that stands out (Willowmere Acres) as attached.
4. Front side must have product name and net weight.
5. Back side must have enough space for Nutrition Fact, product descriptions (110 mm * 100 mm), and barcode.
6. Back side must have white space to print production and expiry dates about 25 mm * 30 mm.
7. Top and bottom of bag must be opaque and not show product.
Updates
Project Deadline Extended
Reason: Extended period for more new ideas and also for requested modification.
Target Market(s)
Premium market. Type A to B customers as well as professional clients. The product is not a snack. It is for cooking or baking.
Industry/Entity Type
Food Store
Requirements
Must have
- Look unique and stand out from others in the market.
- The colors of the word "Willowmere Acres" and the blue air-brush in the logo can be changed.
Nice to have
- See project description
Should not have
- See project description

```html
<!DOCTYPE html>
<html lang="en">
<head>
<meta charset="utf-8">
<title>Willowmere Acres – Retail Bag Range</title>
<link rel="stylesheet" href="https://fonts.googleapis.com/css2?family=Montserrat:wght@500;700;800&family=Oswald:wght@600&display=swap">
<style>
  :root {
    --page-bg: #ececee;
    --bag-face: #f4f4f5;
    --bag-edge: #dcdcdf;
    --seal-line: #e2e2e5;
    --brand-blue: #2b3a8f;
    --seeds-accent: #5d2a87;
    --seeds-badge: #5a2a80;
    --nuts-accent: #7b4a22;
    --nuts-badge: #5c3a22;
    --weight-text: #ffffff;
  }
  * { box-sizing: border-box; margin: 0; padding: 0; }
  html, body { width: 1200px; height: 1200px; overflow: hidden; }
  body {
    background: var(--page-bg);
    font-family: "Montserrat", Arial, sans-serif;
    position: relative;
  }
  .bag {
    position: absolute;
    top: 270px;
    width: 420px;
    height: 610px;
    background: var(--bag-face);
    border: 1px solid var(--bag-edge);
    border-radius: 6px 6px 14px 14px;
  }
  .bag--seeds { left: 100px; --accent: var(--seeds-accent); --badge: var(--seeds-badge); }
  .bag--nuts  { left: 680px; --accent: var(--nuts-accent);  --badge: var(--nuts-badge); }
  .bag__seal {
    position: absolute; left: 0; right: 0; top: 64px;
    border-top: 2px solid var(--seal-line);
  }
  .brand {
    position: absolute; top: 120px; left: 0; right: 0;
    display: flex; align-items: center; justify-content: center; gap: 10px;
    color: var(--brand-blue);
    font-weight: 700; font-size: 26px; letter-spacing: 0.5px;
  }
  .brand__dot {
    width: 14px; height: 14px; border-radius: 50%;
    background: var(--brand-blue);
  }
  .tagline {
    position: absolute; top: 244px; left: 0; right: 0;
    display: flex; align-items: center; justify-content: center; gap: 8px;
    color: var(--accent);
    font-weight: 500; font-size: 13px; letter-spacing: 5px;
  }
  .tagline::before, .tagline::after {
    content: ""; width: 58px; border-top: 1.5px solid var(--accent);
  }
  .product-name {
    position: absolute; top: 262px; left: 0; right: 0;
    text-align: center;
    color: var(--accent);
    font-family: "Oswald", "Arial Narrow", sans-serif;
    font-weight: 600; font-size: 44px; letter-spacing: 2px; word-spacing: 10px;
  }
  .window {
    position: absolute; top: 320px; left: 50%;
    width: 180px; height: 180px; margin-left: -90px;
    border-radius: 50%;
  }
  .bag--seeds .window { background: radial-gradient(circle at 45% 40%, #f3ead2, #dccfa9 70%, #c9b98e); }
  .bag--nuts .window  { background: radial-gradient(circle at 60% 35%, #e8d4b0, #a8653a 55%, #6e3520); }
  .claims {
    position: absolute; top: 508px; left: 0; right: 0;
    display: flex; justify-content: center; gap: 8px;
  }
  .claim {
    width: 46px; height: 46px; border-radius: 50%;
    background: var(--badge);
    color: #fff; font-weight: 800; font-size: 11px; line-height: 10px;
    display: flex; flex-direction: column; align-items: center; justify-content: center;
    letter-spacing: 0.5px;
  }
  .claim span:last-child { font-weight: 500; font-size: 10px; }
  .net-weight {
    position: absolute; top: 575px; left: 0; right: 0;
    text-align: center;
    color: var(--weight-text);
    font-weight: 800; font-size: 12px;
    text-shadow: 0 0 2px rgba(0,0,0,0.25);
  }
</style>
</head>
<body>
  <section class="bag bag--seeds">
    <div class="bag__seal"></div>
    <div class="brand"><span class="brand__dot"></span>Willowmere Acres</div>
    <p class="tagline">PREMIUM</p>
    <h1 class="product-name">PUMPKIN SEEDS</h1>
    <div class="window" role="img" aria-label="Clear window showing shelled pumpkin seeds"></div>
    <div class="claims">
      <div class="claim"><span>HEA</span><span>LTHY</span></div>
      <div class="claim"><span>NAT</span><span>URAL</span></div>
      <div class="claim"><span>ORG</span><span>ANIC</span></div>
    </div>
    <p class="net-weight">200G</p>
  </section>

  <section class="bag bag--nuts">
    <div class="bag__seal"></div>
    <div class="brand"><span class="brand__dot"></span>Willowmere Acres</div>
    <p class="tagline">PREMIUM</p>
    <h1 class="product-name">DRIED NUTS</h1>
    <div class="window" role="img" aria-label="Clear window showing mixed hazelnuts, almonds and cashews"></div>
    <div class="claims">
      <div class="claim"><span>HEA</span><span>LTHY</span></div>
      <div class="claim"><span>NAT</span><span>URAL</span></div>
      <div class="claim"><span>ORG</span><span>ANIC</span></div>
    </div>
    <p class="net-weight">200G</p>
  </section>
</body>
</html>
```